Bright Meadow Counseling Business Card design with a visually interesting use of Space

I need business cards that are luxurious and give a peaceful, calm vibe. I also had some letterhead designed, and i like the look of it also, it's attached with the logo design for reference/ ideas but feel free to be creative.

Target Market(s)

High end luxurious client who needs counseling

Industry/Entity Type

Marriage and Family Therapy

Contact Information for Business Card

Mira Kowalczyk MS LMFT/ or Toby Hallett address 4150 Larkin Suite 600

Font styles to use
Sans Serif

Colors
0054AA
0677BA
7BADD7
CADEEF
E8F1F8
0094D4
00A9DD
6FCCEA
C7EBF8
E9F6FB
A7469A
B969AE
D3A5CF
EDDBEB
F8F0F9
6B429C
8869AF
B7A5CE
E3DAEB
F3F0F8

Requirements
Must have
• Logo and color scheme but be simple modern and luxurious
Nice to have
• I'd like to incorporate some elelmets from the logo and letterhead into a simple modern card

```html
<!DOCTYPE html>
<html lang="en">
<head>
<meta charset="utf-8">
<title>Bright Meadow Counseling – Business Card</title>
<link rel="stylesheet" href="https://fonts.googleapis.com/css2?family=Lato:wght@300;400;700&display=swap">
<style>
  :root {
    --bg: #dcdde0;
    --paper: #ffffff;
    --teal: #12a79a;
    --ink: #3b3b3b;
    --sky: #6fccea;
    --cyan: #00a9dd;
    --blue: #0677ba;
    --navy: #0054aa;
    --violet: #8869af;
    --plum: #6b429c;
    --magenta: #a7469a;
    --orchid: #b969ae;
    --icon: #a7469a;
  }
  * { box-sizing: border-box; margin: 0; padding: 0; }
  html, body { width: 1200px; height: 800px; overflow: hidden; }
  body {
    background: var(--bg);
    font-family: "Lato", sans-serif;
    display: flex;
    align-items: center;
    justify-content: center;
    gap: 40px;
  }
  .card {
    position: relative;
    width: 540px;
    height: 309px;
    background: var(--paper);
    overflow: hidden;
    box-shadow: 0 10px 24px rgba(0,0,0,0.12);
  }

  /* Front */
  .front-field {
    position: absolute;
    inset: 14px 10px 14px 10px;
    border-radius: 48px 140px 40px 160px;
    background:
      radial-gradient(circle at 20% 30%, rgba(111,204,234,0.9), transparent 45%),
      radial-gradient(circle at 60% 40%, rgba(6,119,186,0.85), transparent 45%),
      radial-gradient(circle at 78% 80%, rgba(167,70,154,0.85), transparent 45%),
      radial-gradient(circle at 25% 75%, rgba(136,105,175,0.9), transparent 50%),
      linear-gradient(135deg, var(--sky), var(--violet) 55%, var(--orchid));
  }
  .front-title {
    position: absolute;
    left: 170px;
    top: 112px;
    color: var(--paper);
    font-weight: 300;
    font-size: 38px;
    line-height: 1;
    letter-spacing: 0.5px;
  }
  .front-title .sub {
    display: block;
    margin: 6px 0 0 78px;
    font-size: 19px;
    letter-spacing: 5px;
  }

  /* Back */
  .back-field {
    position: absolute;
    left: -20px;
    top: 70px;
    width: 230px;
    height: 230px;
    border-radius: 40% 60% 55% 45%;
    background:
      radial-gradient(circle at 35% 25%, rgba(0,169,221,0.85), transparent 45%),
      radial-gradient(circle at 70% 55%, rgba(0,84,170,0.8), transparent 45%),
      radial-gradient(circle at 70% 85%, rgba(167,70,154,0.85), transparent 45%),
      linear-gradient(160deg, var(--sky), var(--violet) 60%, var(--magenta));
  }
  .brand {
    position: absolute;
    left: 34px;
    top: 30px;
    color: var(--ink);
    font-weight: 300;
    font-size: 27px;
    line-height: 1;
  }
  .brand .sub {
    display: block;
    margin: 4px 0 0 54px;
    font-size: 13px;
    letter-spacing: 3.5px;
  }
  .brand-dot {
    position: absolute;
    left: 268px;
    top: 30px;
    width: 34px;
    height: 34px;
    border-radius: 50%;
    background: var(--violet);
  }
  .person {
    position: absolute;
    right: 30px;
    top: 108px;
    text-align: right;
    color: var(--teal);
  }
  .person .name { font-weight: 700; font-size: 21px; }
  .person .cred { font-weight: 400; font-size: 12px; margin-top: 2px; letter-spacing: 0.5px; }
  .contact {
    position: absolute;
    right: 30px;
    top: 178px;
    list-style: none;
    text-align: right;
    color: var(--ink);
    font-size: 13px;
    line-height: 21px;
  }
  .contact li { display: flex; align-items: center; justify-content: flex-end; gap: 7px; }
  .contact svg { width: 11px; height: 11px; fill: var(--icon); flex: none; }
</style>
</head>
<body>

  <section class="card card-front">
    <div class="front-field" role="img" aria-label="Soft field of overlapping blue, violet and magenta tones"></div>
    <h1 class="front-title">Bright Meadow<span class="sub">Counseling</span></h1>
  </section>

  <section class="card card-back">
    <div class="back-field" role="img" aria-label="Soft cluster of blue, violet and magenta tones"></div>
    <div class="brand">Bright Meadow<span class="sub">Counseling</span></div>
    <span class="brand-dot"></span>

    <div class="person">
      <div class="name">Mira Kowalczyk</div>
      <div class="cred">MS LMFT</div>
    </div>

    <ul class="contact">
      <li>555-214-7730
        <svg viewBox="0 0 24 24"><path d="M6.6 10.8a15 15 0 0 0 6.6 6.6l2.2-2.2c.3-.3.7-.4 1-.2 1.1.4 2.3.6 3.6.6.6 0 1 .4 1 1V20c0 .6-.4 1-1 1A17 17 0 0 1 3 4c0-.6.4-1 1-1h3.5c.6 0 1 .4 1 1 0 1.3.2 2.5.6 3.6.1.3 0 .7-.2 1z"/></svg></li>
      <li>555-214-7731
        <svg viewBox="0 0 24 24"><path d="M6 2h9l3 3v5H6zM3 11h18v9H3zm3 6h12v-2H6z"/></svg></li>
      <li>4150 Larkin Suite 600
        <svg viewBox="0 0 24 24"><path d="M12 2a7 7 0 0 0-7 7c0 5 7 13 7 13s7-8 7-13a7 7 0 0 0-7-7zm0 9.5A2.5 2.5 0 1 1 12 6.5a2.5 2.5 0 0 1 0 5z"/></svg></li>
      <li>info@brightmeadow.com
        <svg viewBox="0 0 24 24"><path d="M2 5h20v14H2zm2 2v.5l8 5 8-5V7z"/></svg></li>
      <li>www.brightmeadow.com
        <svg viewBox="0 0 24 24"><path d="M12 2a10 10 0 1 0 0 20 10 10 0 0 0 0-20zm0 2c1.5 1.8 2.4 4.5 2.6 7H9.4c.2-2.5 1.1-5.2 2.6-7zM4.1 13h3.3c.1 2.3.8 4.5 1.8 6.2A8 8 0 0 1 4.1 13zm0-2a8 8 0 0 1 5.1-6.2C8.2 6.5 7.5 8.7 7.4 11zm5.3 2h5.2c-.2 2.5-1.1 5.2-2.6 7-1.5-1.8-2.4-4.5-2.6-7zm5.4 6.2c1-1.7 1.7-3.9 1.8-6.2h3.3a8 8 0 0 1-5.1 6.2zM16.6 11c-.1-2.3-.8-4.5-1.8-6.2A8 8 0 0 1 19.9 11z"/></svg></li>
    </ul>
  </section>

</body>
</html>
```